Tolvane BrandWorks Corporate Site

Design a site to replace www.tolvanebrandworks.com, built for/within net harbor and incorporate numerous corporate assets and lines of business (www.pulsarstageworksinc.com, www.summitoutingpros.com, www.zapsnapkiosk.com, www.nibblecrate.com, www.strumbleorama.com) as well as our consulting and artist management work.

Target Market(s)

businesses, non profits, talent (performing artists)

Industry/Entity Type

Business

Coding

Coded - Design and coding required

Number of Pages Required

5+ page

Colors
0655a3
ffc214

Requirements
Must have
• social media visibility, multi-media

```html
<!DOCTYPE html>
<html lang="en">
<head>
<meta charset="utf-8">
<title>Tolvane BrandWorks</title>
<link rel="stylesheet" href="https://fonts.googleapis.com/css2?family=Montserrat:wght@400;600;700&family=Open+Sans:ital,wght@0,400;0,600;0,700;1,400&family=Playfair+Display:wght@600&display=swap">
<style>
:root{
  --blue:#0655a3;
  --yellow:#ffc214;
  --ink:#444;
  --muted:#888;
  --line:#ddd;
  --pale:#f4f4f4;
  --footer:#1d1d1d;
  --white:#fff;
}
*{box-sizing:border-box;margin:0;padding:0}
html,body{width:1200px;height:2826px;overflow:hidden}
body{position:relative;background:var(--white);font-family:"Open Sans",Arial,sans-serif;color:var(--ink)}
.abs{position:absolute}
.heading{position:absolute;left:0;width:1200px;text-align:center;font-family:"Montserrat",sans-serif;font-size:19px;font-weight:400;letter-spacing:1px;color:#666;text-transform:uppercase}
.heading b{font-weight:600;color:#444}
.heading::after{content:"";display:block;width:40px;height:1px;background:#bbb;margin:14px auto 0}

/* header */
.logo{left:211px;top:14px;font-family:"Playfair Display",serif;font-size:30px;color:var(--blue);line-height:1}
.logo-sub{left:213px;top:46px;font-size:9px;letter-spacing:1.2px;color:var(--blue)}
.search{left:780px;top:24px;width:209px;height:34px;border:1px solid var(--line);display:flex}
.search span{flex:1;font-size:10px;font-style:italic;color:#aaa;padding:11px 12px}
.search i{width:36px;background:var(--blue);display:flex;align-items:center;justify-content:center}
.nav{left:0;top:83px;width:1200px;height:40px;background:var(--yellow)}
.nav .home{position:absolute;left:209px;top:0;width:47px;height:40px;background:var(--blue);display:flex;align-items:center;justify-content:center}
.nav a{position:absolute;top:13px;font-family:"Montserrat",sans-serif;font-size:11px;font-weight:600;color:var(--white);text-decoration:none;letter-spacing:.5px}
.socials{display:flex;gap:6px}
.socials span{width:22px;height:22px;border:1.5px solid currentColor;border-radius:50%}
.nav .socials{position:absolute;left:887px;top:9px;color:var(--white)}

/* hero */
.hero{left:0;top:123px;width:1200px;height:459px;background:linear-gradient(100deg,#8a5a3c 0%,#c9a07e 20%,#e9e1d6 45%,#d7cbc0 65%,#a26a52 85%,#e8e2dc 100%)}
.hero-title{left:0;top:293px;width:1200px;text-align:center;font-family:"Montserrat",sans-serif;font-size:26px;font-weight:600;color:var(--yellow);letter-spacing:1px}
.hero-text{left:300px;top:346px;width:600px;text-align:center;font-size:11px;line-height:17px;color:var(--white);text-transform:uppercase;letter-spacing:.4px}
.btn-yellow{left:535px;top:418px;width:128px;height:32px;background:var(--yellow);color:var(--white);font-family:"Montserrat",sans-serif;font-size:11px;font-weight:600;display:flex;align-items:center;justify-content:center;letter-spacing:1px}
.dots{display:flex;gap:6px;justify-content:center}
.dots span{width:8px;height:8px;border-radius:50%;border:1px solid #fff}
.dots .on{background:var(--yellow);border-color:var(--yellow)}

/* services */
.intro{left:340px;top:697px;width:520px;text-align:center;font-size:10px;line-height:18px;color:#999}
.service{top:759px;width:254px;height:336px;text-align:center}
.service.active{background:var(--yellow);color:var(--white)}
.service .circle{width:110px;height:110px;border:1px solid #bbb;border-radius:50%;margin:28px auto 0;display:flex;align-items:center;justify-content:center}
.service.active .circle{border-color:var(--white)}
.service h3{font-family:"Montserrat",sans-serif;font-weight:400;font-size:13px;margin-top:36px;color:#666}
.service.active h3{color:var(--white)}
.service p{font-size:10px;line-height:17px;margin:20px 28px 0;color:#888}
.service.active p{color:var(--white);font-weight:600}
.service .more{width:90px;height:29px;border:1px solid #bbb;margin:22px auto 0;font-size:9px;letter-spacing:1px;color:#777;display:flex;align-items:center;justify-content:center;background:var(--white)}
.service.active .more{border-color:var(--white);color:var(--yellow)}

/* blog */
.blog-band{left:0;top:1164px;width:1200px;height:584px;background:var(--pale)}
.blog-card{left:260px;top:1328px;width:364px;height:302px;background:var(--white);text-align:center;box-shadow:0 1px 3px rgba(0,0,0,.06)}
.date-box{width:40px;height:32px;background:var(--blue);color:var(--white);font-family:"Montserrat",sans-serif;font-size:20px;font-weight:600;margin:38px auto 0;display:flex;align-items:center;justify-content:center}
.blog-card .month{font-size:11px;color:#888;margin-top:6px;letter-spacing:1px}
.blog-card .by{font-size:8px;color:#999;margin-top:16px}
.blog-card .by em{color:var(--yellow);font-style:normal}
.blog-card h4{font-family:"Montserrat",sans-serif;font-weight:400;font-size:10px;letter-spacing:.5px;margin-top:18px;color:#555}
.blog-card p{font-size:9px;line-height:17px;color:#888;margin:12px 40px 0}
.btn-outline{width:94px;height:30px;border:1px solid #ccc;margin:22px auto 0;font-size:9px;letter-spacing:1px;color:#888;display:flex;align-items:center;justify-content:center}
.pager{display:flex;gap:5px;justify-content:center;margin-top:18px}
.pager span{width:8px;height:8px;border:1px solid #aaa;border-radius:50%}
.pager .on{background:var(--blue);border-color:var(--blue)}
.blog-photo{left:593px;top:1309px;width:332px;height:343px;background:linear-gradient(90deg,#2c2a28,#8b8d90 30%,#d9dcdf 50%,#6c6e70 70%,#2a2827)}

/* news */
.news{top:1859px;width:246px}
.news .photo{height:157px}
.news h5{font-size:12px;font-weight:400;line-height:17px;margin-top:13px;color:#555}
.news h5.blue{color:var(--blue)}
.news .date{font-size:9px;font-style:italic;margin-top:9px;color:var(--yellow)}
.news .date.grey{color:#777}
.divider{left:0;top:2144px;width:1200px;height:1px;background:#eee}

/* clients */
.clients{left:260px;top:2266px;width:665px;display:grid;grid-template-columns:repeat(5,124px);gap:15px 11px}
.client{height:55px;border:1px solid #e3e3e3;display:flex;align-items:center;justify-content:center;gap:6px;font-family:"Open Sans",sans-serif;font-size:10px;font-weight:700;color:var(--blue);text-align:center}
.client i{width:10px;height:10px;background:var(--blue);flex:none}
.squares{left:0;top:2432px;width:1200px;display:flex;gap:3px;justify-content:center}
.squares span{width:8px;height:7px;background:#777}
.squares .on{background:var(--yellow)}

/* footer */
.footer{left:0;top:2479px;width:1200px;height:347px;background:var(--footer);color:#bbb}
.f-head{position:absolute;top:82px;font-family:"Montserrat",sans-serif;font-size:13px;font-weight:400;letter-spacing:.5px;color:#ddd}
.f-about{position:absolute;left:209px;top:130px;width:200px;font-size:9px;line-height:19px;color:#aaa}
.f-post{position:absolute;left:454px;width:180px}
.f-post b{display:block;font-size:10px;line-height:19px;font-weight:600;color:#ddd}
.f-post span{display:block;font-size:8px;font-style:italic;color:#999;margin-top:4px}
.f-links{position:absolute;left:665px;top:128px;list-style:none}
.f-links li{font-size:10px;line-height:21.4px;color:#bbb}
.f-links li::before{content:"\00bb";color:#888;margin-right:8px}
.f-input{position:absolute;left:808px;top:106px;width:181px;height:32px;border:1px solid #888;font-size:10px;font-style:italic;color:#bbb;padding:9px 12px}
.f-note{position:absolute;left:808px;top:156px;font-size:10px;color:#bbb}
.f-rule{position:absolute;left:209px;top:302px;width:780px;height:1px;background:#3a3a3a}
.f-copy{position:absolute;left:209px;top:320px;font-size:9px;color:#999}
.footer .socials{position:absolute;left:893px;top:314px;color:#aaa}
.footer .socials span{width:20px;height:20px}
</style>
</head>
<body>

<header>
  <div class="abs logo">Tolvane BrandWorks</div>
  <div class="abs logo-sub">STRATEGIC MARKETING &amp; COMMUNICATIONS</div>
  <div class="abs search"><span>Search Keyword</span><i><svg width="12" height="12" viewBox="0 0 12 12"><circle cx="5" cy="5" r="3.5" fill="none" stroke="#fff" stroke-width="1.5"/><path d="M7.5 7.5 11 11" stroke="#fff" stroke-width="1.8"/></svg></i></div>
</header>

<nav class="abs nav">
  <div class="home"><svg width="16" height="14" viewBox="0 0 16 14"><path d="M8 0 16 7H13V14H9.5V9.5H6.5V14H3V7H0Z" fill="#fff"/></svg></div>
  <a style="left:281px">ABOUT US</a>
  <a style="left:376px">SERVICES</a>
  <a style="left:462px">CLIENTS</a>
  <a style="left:541px">NEWS &amp; EVENTS</a>
  <a style="left:659px">BLOG</a>
  <a style="left:727px">CONTACT US</a>
  <div class="socials" aria-label="Social links"><span></span><span></span><span></span><span></span></div>
</nav>

<section>
  <div class="abs hero" role="img" aria-label="Team gathered around a table with sticky notes, brainstorming"></div>
  <svg class="abs" style="left:82px;top:344px" width="14" height="28" viewBox="0 0 14 28"><path d="M12 2 2 14 12 26" fill="none" stroke="#fff" stroke-width="2"/></svg>
  <svg class="abs" style="left:1104px;top:344px" width="14" height="28" viewBox="0 0 14 28"><path d="M2 2 12 14 2 26" fill="none" stroke="#fff" stroke-width="2"/></svg>
  <div class="abs hero-title">COMMUNICATE * COLLABORATE * CELEBRATE</div>
  <div class="abs hero-text">From experiential learning and event based teambuilding and leadership development to full service event management and entertainment programming</div>
  <div class="abs btn-yellow">LEARN MORE</div>
  <div class="abs dots" style="left:0;top:538px;width:1200px"><span></span><span class="on"></span><span></span><span></span></div>
</section>

<section>
  <h2 class="heading" style="top:648px">We meet your strategic <b>marketing &amp; communication</b></h2>
  <p class="abs intro">Sed ut perspiciatis unde omnis iste natus error sit voluptatem accusantium doloremque laudantium, totam rem aperiam, eaque ipsa quae ab illo inventore veritatis et quasi architecto beatae vitae dicta.</p>

  <div class="abs service" style="left:203px">
    <div class="circle"><svg width="44" height="30" viewBox="0 0 44 30"><path d="M2 10 12 4 20 8 28 4 42 10 34 22 26 26 18 22 10 20Z" fill="#999"/></svg></div>
    <h3>Public Relations</h3>
    <p>Nemo enim ipsam voluptatem quia voluptas sit aspernatur aut odit aut fugit, sed quia consequuntur</p>
    <div class="more">LEARN MORE</div>
  </div>
  <div class="abs service active" style="left:469px">
    <div class="circle"><svg width="40" height="40" viewBox="0 0 40 40" fill="#fff" stroke="#fff" stroke-width="1.5"><line x1="20" y1="20" x2="20" y2="5"/><line x1="20" y1="20" x2="34" y2="14"/><line x1="20" y1="20" x2="32" y2="32"/><line x1="20" y1="20" x2="8" y2="32"/><line x1="20" y1="20" x2="6" y2="14"/><circle cx="20" cy="20" r="6"/><circle cx="20" cy="5" r="3"/><circle cx="34" cy="14" r="3"/><circle cx="32" cy="32" r="3"/><circle cx="8" cy="32" r="3"/><circle cx="6" cy="14" r="3"/></svg></div>
    <h3>Strategic Marketing</h3>
    <p>Nemo enim ipsam voluptatem quia voluptas sit aspernatur aut odit aut fugit, sed quia consequuntur</p>
    <div class="more">LEARN MORE</div>
  </div>
  <div class="abs service" style="left:734px">
    <div class="circle"><svg width="36" height="36" viewBox="0 0 36 36"><circle cx="18" cy="18" r="16" fill="#999"/><path d="M10 10h8v6h-6zM20 20h8v8h-6z" fill="#fff"/></svg></div>
    <h3>Multicultural Marketing</h3>
    <p>Nemo enim ipsam voluptatem quia voluptas sit aspernatur aut odit aut fugit, sed quia consequuntur</p>
    <div class="more">LEARN MORE</div>
  </div>
</section>

<section>
  <div class="abs blog-band"></div>
  <h2 class="heading" style="top:1236px">Latest <b>blog</b></h2>
  <div class="abs blog-photo" role="img" aria-label="Snowy forest with tall bare tree trunks"></div>
  <article class="abs blog-card">
    <div class="date-box">14</div>
    <div class="month">MAY</div>
    <div class="by">by <em>Marcus Vell</em></div>
    <h4>THE ADVENTURE AWAITS!</h4>
    <p>And once workforce balance has been achieved, ignite its capacity with transformational teambuilding programs!</p>
    <div class="btn-outline">READ MORE</div>
    <div class="pager"><span></span><span class="on"></span><span></span></div>
  </article>
</section>

<section>
  <h2 class="heading" style="top:1803px">In the <b>news</b></h2>
  <article class="abs news" style="left:209px">
    <div class="photo" role="img" aria-label="Person at a desk working on a computer" style="background:linear-gradient(160deg,#e8e4de,#c9a56a 55%,#6d5a44)"></div>
    <h5 class="blue">Pulsar Stageworks completes 12 events over the 5/13/11 weekend</h5>
    <div class="date grey">May13, 2011</div>
  </article>
  <article class="abs news" style="left:477px">
    <div class="photo" role="img" aria-label="Small tricycle in a room with a ladder" style="background:linear-gradient(160deg,#cfc8bf,#a89d92 50%,#5b4a44)"></div>
    <h5>Vantelle Selects Tolvane BrandWorks Inc. To Support College Recruiting in 2011</h5>
    <div class="date">May12, 2011</div>
  </article>
  <article class="abs news" style="left:742px">
    <div class="photo" role="img" aria-label="Business meeting with laptop and documents on a table" style="background:linear-gradient(160deg,#2b3b5a,#d8dde3 50%,#394a6a)"></div>
    <h5>Tolvane BrandWorks Inc. President Newly Appointed To Positive</h5>
    <div class="date">May12, 2011</div>
  </article>
  <div class="abs divider"></div>
</section>

<section>
  <h2 class="heading" style="top:2198px">Great integration with our <b>clients</b></h2>
  <div class="abs clients">
    <div class="client"><i></i>Quillmere College</div>
    <div class="client"><i></i>Riverbend Medical</div>
    <div class="client"><i></i>Skyline Hoopers</div>
    <div class="client"><i></i>Northgate Tech</div>
    <div class="client"><i></i>Fizzwell</div>
    <div class="client"><i></i>Dunmore Chamber</div>
    <div class="client"><i></i>Redstone Power</div>
    <div class="client"><i></i>Kestrel Construction</div>
    <div class="client"><i></i>Lakeshire Chamber</div>
    <div class="client"><i></i>Corvane</div>
  </div>
  <div class="abs squares"><span class="on"></span><span></span><span></span><span></span></div>
</section>

<footer class="abs footer">
  <h6 class="f-head" style="left:209px">ABOUT US</h6>
  <p class="f-about">Is your marketing and communications partner responsive, and flexible? Creative, yet practical? Do they understand your business enough to be strategic? Do they care enough to be passionate? Your business deserves no less. In fact, it deserves much more.</p>

  <h6 class="f-head" style="left:454px">RECENT NEWS</h6>
  <div class="f-post" style="top:126px"><b>Within the construction industry as their overdraft</b><span>January 22, 2016</span></div>
  <div class="f-post" style="top:190px"><b>Within the construction industry as their overdraft</b><span>January 22, 2016</span></div>

  <h6 class="f-head" style="left:665px">SITE LINKS</h6>
  <ul class="f-links"><li>Home</li><li>About Us</li><li>Our Services</li><li>Clients</li><li>News &amp; Events</li><li>Blog</li><li>Contact</li></ul>

  <h6 class="f-head" style="left:808px">SUBSCRIBE</h6>
  <div class="f-input">Email Address</div>
  <svg class="abs" style="left:963px;top:117px" width="16" height="11" viewBox="0 0 16 11"><rect width="16" height="11" fill="#ccc"/><path d="M0 0 8 6 16 0" fill="none" stroke="#1d1d1d"/></svg>
  <p class="f-note">Get latest updates and offers.</p>

  <div class="f-rule"></div>
  <p class="f-copy">© Copyright 2016, Tolvane BrandWorks. All Rights Reserved</p>
  <div class="socials" aria-label="Social links"><span></span><span></span><span></span><span></span></div>
</footer>

</body>
</html>
```